Business Card desgin, company called Tall Orbit.

I am looking for the logo colors (3) to be used on the card in whatever design you think might work. the certifications are on the back (4) on the front will be my name, Dana Whitlock, owner/instructor, phone 317.582.4096, website www.tlo-coaching.example, email dw@tlo-coaching.example. im flexible on fonts.

Target Market(s)

firearms owners

Industry/Entity Type

firearms training

Contact Information for Business Card

certification icons on back

```html
<!DOCTYPE html>
<html lang="en">
<head>
<meta charset="utf-8">
<title>Tall Orbit – Business Card</title>
<link href="https://fonts.googleapis.com/css2?family=Montserrat:wght@400;500;700;800&family=Playfair+Display:wght@500&display=swap" rel="stylesheet">
<style>
  :root {
    --navy: #0e2a48;
    --red: #e11b2a;
    --white: #ffffff;
    --ink: #2b2b2b;
    --rule: #b9bec6;
    --stage: #5a5c60;
    --badge-orange: #f08a1c;
    --badge-dark: #1e1e1e;
    --badge-blue: #1f4f8f;
  }
  * { margin: 0; padding: 0; box-sizing: border-box; }
  html, body { width: 1200px; height: 1200px; overflow: hidden; }
  body {
    background: var(--stage);
    font-family: "Montserrat", sans-serif;
    position: relative;
  }
  .card {
    position: absolute;
    left: 150px;
    width: 900px;
    height: 514px;
    border-radius: 36px;
    overflow: hidden;
    box-shadow: 0 14px 30px rgba(0,0,0,0.35);
  }
  .card--front { top: 60px; background: var(--white); }
  .card--back { top: 626px; background: var(--navy); border-bottom: 5px solid var(--red); }

  .front-bands { position: absolute; inset: 0; }

  .brand {
    position: absolute;
    top: 44px;
    left: 0;
    width: 900px;
    display: flex;
    flex-direction: column;
    align-items: center;
    gap: 18px;
  }
  .brand__dot {
    width: 96px; height: 96px;
    border-radius: 50%;
    border: 9px solid var(--navy);
  }
  .brand__name {
    color: var(--navy);
    font-weight: 800;
    font-size: 50px;
    line-height: 1.1;
    letter-spacing: 3px;
    text-transform: uppercase;
  }

  .divider {
    position: absolute;
    left: 480px; top: 250px;
    width: 2px; height: 130px;
    background: var(--rule);
  }

  .contact {
    position: absolute;
    left: 505px; top: 250px;
    list-style: none;
    display: flex; flex-direction: column; gap: 12px;
  }
  .contact__item {
    display: flex; align-items: center; gap: 12px;
    font-size: 23px; line-height: 28px; color: var(--ink); font-weight: 400;
    white-space: nowrap;
  }
  .contact__icon { width: 28px; height: 28px; flex: none; }

  .person { position: absolute; left: 60px; top: 262px; }
  .person__name {
    color: var(--red); font-weight: 700; font-size: 36px; line-height: 1.15;
    text-transform: uppercase; letter-spacing: 1px; white-space: nowrap;
  }
  .person__role {
    color: var(--ink); font-weight: 400; font-size: 22px; line-height: 1.2;
    text-transform: uppercase; letter-spacing: 1px; margin-top: 4px;
  }

  .badges {
    position: absolute; left: 60px; top: 358px;
    display: flex; gap: 30px; align-items: flex-end;
  }
  .badge { width: 64px; height: 70px; }

  .back-mark {
    position: absolute; left: 110px; top: 175px;
    width: 170px; height: 170px; border-radius: 50%;
    border: 14px solid var(--white);
  }
  .back-text { position: absolute; left: 320px; top: 188px; }
  .back-text__name {
    color: var(--red); font-weight: 800; font-size: 66px;
    letter-spacing: 3px; text-transform: uppercase; line-height: 1;
  }
  .back-text__url {
    color: var(--white); font-family: "Playfair Display", serif;
    font-weight: 500; font-size: 38px; margin-top: 18px; white-space: nowrap;
  }
</style>
</head>
<body>

<section class="card card--front" aria-label="Card front">
  <svg class="front-bands" width="900" height="514" viewBox="0 0 900 514" aria-hidden="true">
    <polygon points="0,486 630,420 620,514 0,514" fill="var(--red)"/>
    <polygon points="646,418 900,372 900,514 636,514" fill="var(--navy)"/>
  </svg>

  <div class="brand">
    <div class="brand__dot" aria-hidden="true"></div>
    <div class="brand__name">Tall Orbit</div>
  </div>

  <div class="divider" aria-hidden="true"></div>

  <ul class="contact">
    <li class="contact__item">
      <svg class="contact__icon" viewBox="0 0 24 24" aria-hidden="true"><path fill="var(--red)" d="M6.6 10.8c1.4 2.8 3.8 5.1 6.6 6.6l2.2-2.2c.3-.3.7-.4 1-.2 1.1.4 2.3.6 3.6.6.6 0 1 .4 1 1V20c0 .6-.4 1-1 1C10.6 21 3 13.4 3 4c0-.6.4-1 1-1h3.5c.6 0 1 .4 1 1 0 1.3.2 2.5.6 3.6.1.3 0 .7-.2 1z"/></svg>
      <span>317.582.4096</span>
    </li>
    <li class="contact__item">
      <svg class="contact__icon" viewBox="0 0 24 24" aria-hidden="true"><rect x="2" y="5" width="20" height="14" fill="var(--red)"/><path d="M2 5l10 8 10-8" fill="none" stroke="var(--white)" stroke-width="1.6"/></svg>
      <span>dw@tlo-coaching.example</span>
    </li>
    <li class="contact__item">
      <svg class="contact__icon" viewBox="0 0 24 24" aria-hidden="true"><g fill="none" stroke="var(--red)" stroke-width="1.6"><circle cx="12" cy="12" r="9.5"/><ellipse cx="12" cy="12" rx="4.5" ry="9.5"/><path d="M2.5 12h19M4 7h16M4 17h16"/></g></svg>
      <span>www.tlo-coaching.example</span>
    </li>
  </ul>

  <div class="person">
    <div class="person__name">Dana Whitlock</div>
    <div class="person__role">Owner/Instructor</div>
  </div>

  <div class="badges">
    <svg class="badge" viewBox="0 0 64 70" role="img" aria-label="Certification badge"><path d="M32 4l26 8v22c0 16-12 28-26 32C18 62 6 50 6 34V12z" fill="var(--badge-blue)"/></svg>
    <svg class="badge" viewBox="0 0 64 70" role="img" aria-label="Certification badge"><path d="M32 4l26 8v22c0 16-12 28-26 32C18 62 6 50 6 34V12z" fill="var(--badge-orange)"/></svg>
    <svg class="badge" viewBox="0 0 64 70" role="img" aria-label="Certification badge"><rect x="6" y="6" width="52" height="58" rx="8" fill="var(--badge-dark)"/></svg>
    <svg class="badge" viewBox="0 0 64 70" role="img" aria-label="Certification badge"><rect x="6" y="6" width="52" height="58" rx="8" fill="var(--badge-dark)"/></svg>
  </div>
</section>

<section class="card card--back" aria-label="Card back">
  <div class="back-mark" aria-hidden="true"></div>
  <div class="back-text">
    <div class="back-text__name">Tall Orbit</div>
    <div class="back-text__url">WWW.TLO-Coaching.example</div>
  </div>
</section>

</body>
</html>
```